MIRA Real Estate Prospecting DL Flyer

I need a DL size (99mm x 210mm) two sided flyer designed for letter boxing and also handing to prospective clients when door knocking across my sales area in Melbourne, Australia. PLEASE NOTE: the flyer is a flat flyer to be designed on both sides as per my doc below. The flyer will likely be printed on 350gsm card. It will not be posted - so NO space for address required. It is for door-knocking (door to door sales) and letter boxing (dropped personally by me in a letterbox - not posted).
My original company logo design brief was that it should be modern and premium black on white and white on black - drawing influences by TEVAN KORL and also FELISTRA. I want my DL flyer to reflect the same influence. I have attached proposed copy on the word document attached below.
The DL flyer will be printed on 350 gsm - probably gloss to reflect the premium feel, but open to suggestion. It is important for the flyer to be durable and have decent shelf life - I am not going for cheap and cheerful on this project. I need to make an impact. I am trying to attract home owners to my business to list and sell their properties - usually for most people their biggest asset is their home/property - so it is important that my business is credible and very experienced (which of course it is).
For a view of the types of properties I sell please go to www.homefindly.com.au and type in Mount Corrandale, Victoria; and also Glen Pellingham, Victoria. You will see a list of properties come up that are either for SALE or for SALE BY AUCTION. This may help with your understanding. The areas I concentrate on are very suburban - meaning families, families, families :)

Target Market(s)

Property owners across the middle ring of eastern suburbs of Melbourne. Value of homes are between $1m and $2m, and mostly consist of 3 and 4 bedroom family homes. Clients range from the elderly looking to downsize to a smaller property, to families looking to sell and upgrade their homes.

Industry/Entity Type

Real Estate Agent

Font styles to use
Serif

Colors
000000
ffffff

Requirements
Must have
• The "call to action" components that I have included on the doc file and include a FREE E-BOOK on supply of their contact details; and a FREE PROFESSIONAL HOME STYLIST CONSULTATION.
• It must feature my company logo. My corporate colours are black and white - so best to stick with these in the design.
• UPDATE: Just call the e-book "7 QUICK STEPS TO RAISE THE FINAL OFFER ON YOUR HOUSE"
• ...forget the City of Tarrowby and City of Bellingrove part!!
• UPDATE: Designs I have liked the best include the following elements:
• 1. Strong brand at top of each side of flyer
• 2. Family pic page 1; property pic page 2
• 3. BOLD Headings
• 4. Amplified CALL TO ACTION - FREE......consult; FREE E-Book
• 5. Clear visible contact details at bottom of page
Nice to have
• Lifestyle photography of homes.
• Some designers have used Asian families in their pics - which is smart as the main buyer demographic is Chinese families. The mail ownership is Australian - so a mix of Asian and Anglo is fine. Try and avoid overtly USA style properties - as Melbourne styles are different. Keys, handshakes etc are all good :)
Should not have
• Animation, cartoons, or visual drawings included.

```html
<!DOCTYPE html>
<html lang="en">
<head>
<meta charset="utf-8">
<title>MIRA Real Estate – DL Flyer</title>
<link rel="stylesheet" href="https://fonts.googleapis.com/css2?family=Montserrat:wght@500&family=Raleway:wght@300;400;500&family=Crimson+Text:wght@400&display=swap">
<style>
  :root{
    --ink:#111111;
    --panel:#1f1f1f;
    --paper:#ffffff;
    --stage:#e6e6e6;
    --soft:#cfcfcf;
    --muted:#8a8a8a;
  }
  *{box-sizing:border-box;margin:0;padding:0}
  html,body{width:1200px;height:794px;overflow:hidden;background:var(--stage)}
  .sheet{position:absolute;top:55px;width:322px;height:683px;background:var(--paper);overflow:hidden;font-family:"Raleway",sans-serif;color:var(--ink)}
  .sheet--front{left:180px}
  .sheet--back{left:566px}
  .abs{position:absolute}
  .nowrap{white-space:nowrap}

  .brand{position:absolute;left:196px;top:0;width:114px;height:69px;background:var(--ink);color:var(--paper);text-align:center;padding-top:16px}
  .brand__name{font-family:"Montserrat",sans-serif;font-weight:500;font-size:30px;letter-spacing:1px;line-height:1}
  .brand__tag{font-family:"Montserrat",sans-serif;font-weight:500;font-size:5px;letter-spacing:4.2px;margin-top:4px}

  /* front */
  .hero-photo{left:14px;top:13px;width:296px;height:256px;background:linear-gradient(180deg,#9fb7a2 0%,#d9d4cc 45%,#a9a49a 75%,#5e6e4d 100%)}
  .front-panel{left:14px;top:285px;width:296px;height:349px;background:var(--panel)}
  .bubble{left:84px;top:241px;width:152px;height:95px}
  .bubble-line{left:84px;width:152px;text-align:center;font-weight:300}
  .bubble__kicker{top:255px;font-size:7.5px;line-height:10px}
  .bubble__mid{top:265px;font-size:11.5px;line-height:12px}
  .bubble__title{top:281px;font-size:20px;line-height:22px;font-variant:small-caps}
  .perks{left:14px;top:319px;list-style:none;color:var(--paper);font-size:9.2px;line-height:12px;font-weight:300}
  .perks li::before{content:"";display:inline-block;width:8px;height:1.5px;background:var(--paper);vertical-align:middle;margin-right:5px}
  .perks__fee{left:27px;top:368px;color:var(--paper);font-size:9.6px;line-height:12px;font-weight:300}
  .perks__fee sup{font-size:5px}
  .intro{left:26px;top:388px;width:186px;color:var(--paper);font-size:6.9px;line-height:12.2px;text-align:justify;font-weight:400}
  .benefits{left:112px;top:478px;width:182px;list-style:none;color:var(--paper);font-size:8.4px;line-height:12.8px;font-weight:400}
  .benefits li{position:relative;padding-left:10px;margin-bottom:4px}
  .benefits li::before{content:"";position:absolute;left:0;top:6px;width:7px;height:1.5px;background:var(--paper)}
  .ebook-kicker{left:14px;top:590px;width:296px;text-align:center;color:var(--soft);font-size:6.5px;line-height:10px}
  .ebook-title{left:31px;top:605px;width:264px;height:26px;background:var(--paper);border:1px solid var(--ink);border-radius:3px;text-align:center;font-size:7px;line-height:24px;font-weight:400}
  .contact-kicker{left:0;top:642px;width:322px;text-align:center;color:var(--muted);font-size:6.5px;line-height:10px}

  /* back */
  .headline{left:20px;top:30px;width:160px;text-align:center;font-weight:300;line-height:1}
  .headline__small{font-size:14px}
  .headline__big{font-size:29px;letter-spacing:-.5px;margin-top:3px}
  .headline__side{font-size:22px;margin-top:3px}
  .headline__side span{font-size:15px}
  .story{left:95px;top:232px;width:230px;text-align:center;font-family:"Crimson Text",serif;font-size:7.8px;line-height:14.7px}
  .story__em{font-size:10.5px;letter-spacing:.4px;line-height:20px}
  .agent-photo{left:14px;top:412px;width:148px;height:271px;background:linear-gradient(180deg,#d8d8d8 0%,#3b3f4a 25%,#23262e 100%)}
  .offer{left:173px;top:479px;width:130px;text-align:center;color:var(--paper);font-size:9.6px;line-height:14.4px;font-weight:300}
  .worth{left:173px;top:563px;width:130px;text-align:center;color:var(--paper);font-size:9.6px;line-height:14px;font-weight:300}
  .price{left:200px;top:580px;width:74px;height:20px}
  .back-contact{left:172px;top:624px;width:140px;height:40px}
</style>
</head>
<body>

<section class="sheet sheet--front">
  <div class="abs hero-photo" role="img" aria-label="Young family holding a toddler in front of a two-storey family home"></div>
  <div class="brand"><div class="brand__name">MIRA</div><div class="brand__tag">REAL ESTATE</div></div>

  <div class="abs front-panel"></div>

  <svg class="abs bubble" viewBox="0 0 152 95" aria-hidden="true">
    <path d="M20 5 Q76 -2 132 5 Q150 9 150 38 Q150 68 132 70 L92 72 L76 92 L67 73 L20 70 Q2 68 2 38 Q2 9 20 5 Z" fill="#fff" stroke="#111" stroke-width="1.2"/>
  </svg>
  <div class="abs bubble-line bubble__kicker">GET THE MAXIMUM</div>
  <div class="abs bubble-line bubble__mid">PRICE FOR</div>
  <div class="abs bubble-line bubble__title">Your Property</div>

  <ul class="abs perks">
    <li>Personal Service</li>
    <li>Clear Communication</li>
    <li>Honest Advice</li>
    <li>Top Results</li>
  </ul>
  <div class="abs perks__fee">For A Fixed Fee <sup>TM</sup></div>

  <p class="abs intro">At MIRA Real Estate we are doing things differently. Our property sales process is designed to extract an ELITE LEVEL PRICE for you, but our cost of doing business is significantly reduced from that of our competitors, and that results in MORE MONEY IN YOUR POCKET.</p>

  <svg class="abs" style="left:210px;top:329px" width="96" height="114" viewBox="0 0 96 114">
    <polygon points="0,22 86,0 96,106 22,114" fill="#fff"/>
    <polygon points="5,25 82,5 91,101 25,108" fill="#d9d2c8" role="img" aria-label="Mother playing with her baby on a sofa"/>
  </svg>

  <svg class="abs" style="left:14px;top:463px" width="86" height="110" viewBox="0 0 86 110">
    <polygon points="0,0 86,22 68,108 0,100" fill="#fff"/>
    <polygon points="4,6 80,25 64,102 4,95" fill="#8a7d6e" role="img" aria-label="Styled master bedroom interior"/>
  </svg>

  <ul class="abs benefits">
    <li>ELITE sales process ensures the maximum possible price for your property.</li>
    <li>Low FIXED FEE TM selling commission – up to half that charged by other agents.</li>
    <li>A FIXED FEE TM in high impact marketing for the sale of your home.</li>
  </ul>

  <div class="abs ebook-kicker">GET YOUR FREE COPY OF MY E-BOOK:</div>
  <div class="abs ebook-title">"7 QUICK STEPS TO RAISE THE FINAL OFFER ON YOUR HOUSE"</div>

  <div class="abs contact-kicker">JUST CALL OR EMAIL:</div>
  <svg class="abs" style="left:16px;top:654px" width="292" height="22" viewBox="0 0 292 22">
    <path d="M2 7 q1 -2 3 -1 l2 3 q0 1 -1 2 q1 3 4 4 q1 -1 2 -1 l3 2 q1 2 -1 3 q-5 1 -9 -3 q-4 -4 -3 -9z" fill="#111"/>
    <text x="13" y="16" font-family="Raleway, sans-serif" font-weight="300" font-size="14" fill="#111" textLength="88" lengthAdjust="spacingAndGlyphs">1800 562 719</text>
    <text x="105" y="16" font-family="Raleway, sans-serif" font-weight="400" font-size="14" fill="#111">|</text>
    <rect x="113" y="8" width="9" height="7" fill="#111"/>
    <path d="M113 8 l4.5 4 l4.5 -4" stroke="#fff" stroke-width=".9" fill="none"/>
    <text x="125" y="16" font-family="Raleway, sans-serif" font-weight="300" font-size="13.5" fill="#111" textLength="165" lengthAdjust="spacingAndGlyphs">sales@mirarealestate.com.au</text>
  </svg>
</section>

<section class="sheet sheet--back">
  <div class="brand"><div class="brand__name">MIRA</div><div class="brand__tag">REAL ESTATE</div></div>

  <div class="abs headline">
    <div class="headline__small">A DECADE OF</div>
    <div class="headline__big">EXPERIENCE</div>
    <div class="headline__side"><span>ON</span> YOUR SIDE</div>
  </div>

  <svg class="abs" style="left:0;top:0" width="322" height="683" viewBox="0 0 322 683">
    <defs>
      <linearGradient id="houseTone" x1="0" y1="0" x2="0" y2="1">
        <stop offset="0" stop-color="#ffffff"/>
        <stop offset=".3" stop-color="#b9b4ac"/>
        <stop offset=".7" stop-color="#8a6e5a"/>
        <stop offset="1" stop-color="#5f7a48"/>
      </linearGradient>
    </defs>
    <polygon points="14,130 310,95 310,110 14,283" fill="url(#houseTone)" role="img" aria-label="Two-storey weatherboard family home with balcony and garden"/>
    <line x1="14" y1="296" x2="310" y2="122" stroke="#111" stroke-width="2"/>
    <polygon points="14,563 310,405 310,669 14,669" fill="#1f1f1f"/>
    <line x1="165" y1="474" x2="310" y2="396" stroke="#111" stroke-width="2"/>
  </svg>

  <div class="abs story nowrap">
    My name's Daniel Mira. With over a decade of<br>
    experience in the property industry<br>
    I know what it takes to get you the<br>
    <span class="story__em">BEST POSSIBLE PRICE</span><br>
    for your property. I've spent much of my career in the<br>
    cutthroat world of commercial property and closing<br>
    high stakes international real estate deals.<br>
    But 3 years ago I brought my expertise<br>
    home to focus on the communities in<br>
    Melbourne's eastern suburbs.<br>
    I've had many incredible sales results to date.<br>
    Will yours be next?
  </div>

  <div class="abs agent-photo" role="img" aria-label="Portrait of the agent in a dark suit and striped tie"></div>

  <div class="abs offer nowrap">Claim Your Free<br>Property Market Appraisal<br>Now And Receive<br>A BONUS Professional<br>Home Stylist Consultation</div>
  <div class="abs worth">Normally Worth</div>
  <svg class="abs price" viewBox="0 0 74 20">
    <polygon points="0,4 8,4 8,16 0,16 4,10" fill="#fff"/>
    <polygon points="74,4 66,4 66,16 74,16 70,10" fill="#fff"/>
    <rect x="9" y="0" width="56" height="20" fill="#fff"/>
    <text x="37" y="16" text-anchor="middle" font-family="Raleway, sans-serif" font-size="15" fill="#111">$118</text>
  </svg>

  <svg class="abs back-contact" viewBox="0 0 140 40">
    <path d="M2 10 q1 -2 3 -1 l2 3 q0 1 -1 2 q1 3 4 4 q1 -1 2 -1 l3 2 q1 2 -1 3 q-5 1 -9 -3 q-4 -4 -3 -9z" fill="#fff"/>
    <text x="16" y="19" font-family="Raleway, sans-serif" font-weight="300" font-size="15.5" fill="#fff" textLength="96" lengthAdjust="spacingAndGlyphs">1800 562 719</text>
    <rect x="6" y="28" width="6" height="4.5" fill="#fff"/>
    <path d="M6 28 l3 2.5 l3 -2.5" stroke="#1f1f1f" stroke-width=".7" fill="none"/>
    <text x="15" y="33" font-family="Raleway, sans-serif" font-size="7.6" fill="#fff" textLength="114" lengthAdjust="spacingAndGlyphs">sales@mirarealestate.com.au</text>
  </svg>
</section>

</body>
</html>
```